Redesign of Bright Harbor Entertainment Card

I already have my logo and font design for my company name. I am looking to come up with a Unique way of having it on my business card. Just looking for a really hip, and professional business card while still using my logo design.

I have also enclosed the front and back of the card so you can see what I have now. Looking for something different.

Thank you!

Target Market(s)

Young to middle aged brides and grooms

Industry/Entity Type

Business

Requirements
Should not have
• Cheese

```html
<!DOCTYPE html>
<html lang="en">
<head>
<meta charset="utf-8">
<title>Bright Harbor Entertainment – Business Card</title>
<link href="https://fonts.googleapis.com/css2?family=Ubuntu:wght@400;500&display=swap" rel="stylesheet">
<style>
  :root {
    --page: #d9dde3;
    --white: #ffffff;
    --sky: #5cc8f4;
    --azure: #2f86e6;
    --royal: #1d47c4;
    --navy: #0b1f7a;
    --ink-blue: #1f3fbf;
    --dash: #2b5cff;
    --tile: #bfeefb;
    --text-light: #f2f7ff;
  }
  * { box-sizing: border-box; margin: 0; padding: 0; }
  html, body { width: 1200px; height: 1000px; overflow: hidden; }
  body {
    background: var(--page);
    font-family: "Ubuntu", sans-serif;
    position: relative;
  }
  .card {
    position: absolute;
    left: 220px;
    width: 760px;
    height: 434px;
    overflow: hidden;
    box-shadow: 0 6px 18px rgba(0,0,0,.18);
  }
  .card--front { top: 50px; background: linear-gradient(180deg, var(--sky) 34%, var(--azure) 62%, var(--royal) 100%); }
  .card--back { top: 516px; background: linear-gradient(135deg, var(--navy) 0%, var(--royal) 55%, var(--sky) 100%); }

  .front__band {
    position: absolute; left: 0; top: 0; width: 100%; height: 150px;
    background: var(--white);
  }
  .brand {
    position: absolute; left: 56px; top: 34px;
    display: flex; align-items: center; gap: 18px;
  }
  .brand__dot {
    width: 66px; height: 66px; border-radius: 50%;
    background: var(--ink-blue);
  }
  .brand__name {
    font-size: 44px; font-weight: 500; color: var(--ink-blue);
    letter-spacing: 1px; line-height: 1;
  }
  .brand__tagline {
    position: absolute; left: 142px; top: 106px;
    font-size: 11px; letter-spacing: 1.6px; color: var(--ink-blue);
    text-transform: uppercase;
  }
  .contact {
    position: absolute; left: 56px; top: 166px;
    color: var(--text-light); font-size: 21px; line-height: 1.36;
  }
  .contact__name { font-size: 27px; font-weight: 500; color: var(--navy); }
  .contact__role { color: var(--navy); font-size: 19px; margin-bottom: 4px; }
  .front__levels {
    position: absolute; right: 40px; top: 150px; width: 160px; height: 90px;
    background: linear-gradient(180deg, rgba(191,238,251,.85), rgba(191,238,251,.35));
  }
  .front__dash { position: absolute; left: 0; bottom: 22px; width: 100%; height: 6px; }

  .back__brand {
    position: absolute; left: 56px; top: 50%; transform: translateY(-50%);
    display: flex; flex-direction: column; align-items: center; gap: 18px;
  }
  .back__dot {
    width: 170px; height: 170px; border-radius: 50%;
    background: var(--white);
  }
  .back__name { font-size: 26px; font-weight: 500; color: var(--text-light); }
  .services {
    position: absolute; right: 60px; top: 90px;
    list-style: none; text-align: right;
    color: var(--text-light); font-size: 26px; line-height: 1.5;
  }
</style>
</head>
<body>
  <section class="card card--front" aria-label="Card front">
    <div class="front__band"></div>
    <div class="brand">
      <span class="brand__dot"></span>
      <span class="brand__name">Bright Harbor</span>
    </div>
    <p class="brand__tagline">Entertainment &amp; Event Professionals</p>
    <div class="contact">
      <p class="contact__name">Evan Marlow</p>
      <p class="contact__role">owner / DJ / emcee</p>
      <p>info@brightharborevents.com</p>
      <p>555-214-7390</p>
      <p>brightharborevents.com</p>
      <p>social: @brightharborentertainment</p>
    </div>
    <div class="front__levels" role="img" aria-label="Decorative equalizer tiles"></div>
    <svg class="front__dash" viewBox="0 0 760 6" preserveAspectRatio="none">
      <line x1="0" y1="3" x2="760" y2="3" stroke="var(--dash)" stroke-width="4" stroke-dasharray="56 18"/>
    </svg>
  </section>

  <section class="card card--back" aria-label="Card back">
    <div class="back__brand">
      <span class="back__dot"></span>
      <span class="back__name">Bright Harbor</span>
    </div>
    <ul class="services">
      <li>Djs / Emcees</li>
      <li>Lighting / Wireless</li>
      <li>LED Uplighting</li>
      <li>Photo Booths</li>
      <li>Photo Montage</li>
    </ul>
  </section>
</body>
</html>
```